Marketplace Web Re-design overhaul @corvahub

Hi,
We are currently in production with a website that is getting some mixed feedback about visual appeal and usability. We are using a responsive design and need to stay true to the logo colours and other marketing collateral we have in place. I will provide a brochure with the colour palate we use for some guidance. If you can please help us design something fresh and modern to communicate the essence of our company. The brochure will be a good summary of what we do and who we are targeting as customers. Our current website can be found at www.corvahub.com. If there is any questions, please let me know.

Target Market(s)

Contractors and Corporate Companies

Industry/Entity Type

Information Technology

Number of Pages Required

4 page

Requirements
Must have
• Must have a complete new visual look, including
• 1. Images
• 2. Background colour scheme overhaul (not black)
• 3. re-design of the layout but keep to similar page breakdowns
Nice to have
• Some of the pages are a bit wordy, happy to have suggestions on how to reduce.
• Would be great if we can integrate the Drift.ON! blog page to the Corvahub page?
• This is some feedback a fellow UX designer provided to improve our CRO
• First off when you land on the home page, who is your audience? Are you everything to everyone? Even after watching the video (https://www.vidplex-example.com/watch?v=q-RtnB7LpX3), I do not know what markets you service or who this app will be for.
• Your main headline and paragraph above the fold I find unnecessarily wordy and an overuse of 'buzzwords' . Perhaps you could look at appealing to the lowest common denominator and make it very simple and put it all into a simple sentence.
• The main hero image to the right of the headline offers no emotional pull at all. I'm assuming it's just a screenshot of your dashboard? Personally, I would be looking at using a person's image in that space.
• Also in this space, increase the size of your 'register' button. On the topic of your register button, you have it in different colours. Green in header, and red in content. Make it the same colour, and don't use that colour again on the site. That colour is to become your call to action (CTA) colour. Understandably you'll have three different colours for the account type, and again, don't use these colours anywhere else on the site.
• The registration area where the three account types are where you choose which one suits you, it's extremely busy with background images and heavy use of text. If you were my client, I would be advising you to ditch the bg image (including the iPad shot), keeping the text, making the register icons much bigger. Perhaps instead of bg images, use a solid colour for each (green, orange, red). I'm highly confident this change will make a massive difference in your sign up rate.
Should not have
• Please keep to the fonts used on the original website
• Keep to the colour provided on the company brochure for guidance.

```html
<!DOCTYPE html>
<html lang="en">
<head>
<meta charset="utf-8">
<title>Corvahub – The Future of Work</title>
<link rel="stylesheet" href="https://fonts.googleapis.com/css2?family=Roboto:wght@300;400;500;700&family=Roboto+Condensed:wght@400;700&display=swap">
<style>
:root{
  --green:#3fa649;
  --green-dark:#2f8c3a;
  --orange:#f7941d;
  --orange-dark:#e0820f;
  --ink:#2b2b2b;
  --text:#666;
  --muted:#999;
  --light:#f2f2f2;
  --grey-band:#e6e6e6;
  --badge:#dcdcdc;
  --dark:#262626;
  --footer:#1f1f1f;
  --white:#fff;
}
*{box-sizing:border-box;margin:0;padding:0}
html,body{width:1200px;height:4401px;overflow:hidden}
body{font-family:"Roboto",Arial,sans-serif;color:var(--text);background:var(--white);position:relative}
.section{position:absolute;left:0;width:1200px}
.wrap{position:relative;width:1030px;margin:0 auto;height:100%}
.btn{display:inline-block;font-size:13px;font-weight:500;color:var(--white);border-radius:3px;padding:11px 20px;text-decoration:none}
.btn-green{background:var(--green)}
.btn-orange{background:var(--orange)}

/* header */
.site-header{top:0;height:112px;background:var(--white)}
.logo{position:absolute;left:0;top:34px;display:flex;align-items:center;gap:10px;font-size:30px;font-weight:400;color:var(--ink)}
.logo i{width:26px;height:26px;border-radius:50%;background:var(--green)}
.nav{position:absolute;right:0;top:40px;display:flex;align-items:center;gap:32px;font-size:13px;font-weight:500;color:var(--ink)}
.nav .active{color:var(--green)}
.nav .login{background:var(--orange);color:var(--white);padding:10px 18px;border-radius:3px}

/* hero */
.hero{top:112px;height:519px;background:linear-gradient(100deg,#16202b 0%,#1d2935 45%,#3a4652 70%,#1c2530 100%)}
.hero-photo{position:absolute;right:0;top:0;width:760px;height:519px;background:radial-gradient(ellipse at 55% 55%,rgba(200,205,210,.35),rgba(0,0,0,0) 60%)}
.hero h1{position:absolute;left:0;top:218px;font-family:"Roboto Condensed",Arial,sans-serif;font-weight:700;font-size:40px;color:var(--white);letter-spacing:.3px}
.hero p{position:absolute;left:0;top:270px;font-family:"Roboto Condensed",Arial,sans-serif;font-weight:700;font-size:34px;color:var(--white)}
.hero .btn{position:absolute;left:0;top:330px;font-size:19px;padding:15px 24px}
.hero-arrows{position:absolute;left:0;top:458px;display:flex;gap:12px}

/* talent */
.talent{top:631px;height:249px;background:var(--light)}
.talent h2{position:absolute;left:0;top:58px;font-size:21px;font-weight:700;color:var(--ink)}
.talent h2 span{color:var(--green)}
.talent p{position:absolute;left:0;top:96px;width:400px;font-size:12.5px;line-height:20px;color:var(--muted)}
.talent .btn{position:absolute;left:0;top:172px;font-size:11px;padding:8px 14px}
.feature{position:absolute;top:40px;width:130px;text-align:center}
.feature svg{display:block;margin:0 auto 16px}
.feature h3{font-size:14px;font-weight:500;color:var(--ink);margin-bottom:14px}
.feature a{font-size:11px;font-weight:500;color:var(--orange);text-decoration:none}

/* welcome */
.welcome{top:880px;height:367px;background:var(--white)}
.video{position:absolute;left:0;top:59px;width:425px;height:249px;border:3px solid #ddd;background:linear-gradient(180deg,#f4f4f4,#e4e4e4)}
.play{position:absolute;left:188px;top:100px}
.welcome h2{position:absolute;left:470px;top:84px;font-size:27px;font-weight:700;color:var(--ink)}
.welcome h2 span{color:var(--orange)}
.welcome p{position:absolute;left:470px;top:132px;width:560px;font-size:13px;line-height:23px;color:var(--text)}
.welcome .btn{position:absolute;left:470px;top:254px;font-size:12px}

/* accounts */
.accounts{top:1247px;height:631px;background:var(--grey-band)}
.account{position:absolute;top:64px;height:508px;padding:30px 50px;color:var(--white)}
.account-contractor{left:0;width:540px;background:var(--orange)}
.account-company{left:514px;width:516px;background:var(--green);border-radius:60px 0 0 0}
.account h2{font-size:24px;font-weight:700}
.account .sub{font-size:12px;font-weight:500;margin-top:4px}
.account .photo{width:400px;height:210px;margin:24px 0 22px}
.account-contractor .photo{background:linear-gradient(135deg,#c9d3dc,#8fa1b0)}
.account-company .photo{background:linear-gradient(135deg,#d8dde2,#a3adb6)}
.account ul{list-style:none;font-size:12px;line-height:25px}
.account li{display:flex;align-items:center;gap:10px}
.account .btn-outline{display:inline-block;margin-top:24px;background:var(--white);font-size:11px;font-weight:700;padding:10px 18px;border-radius:2px}
.account-contractor .btn-outline{color:var(--orange)}
.account-company .btn-outline{color:var(--green)}

/* blog */
.blog{top:1878px;height:601px;background:var(--white)}
.section-title{text-align:center;font-size:24px;font-weight:700;color:var(--ink)}
.section-sub{text-align:center;font-size:12px;color:var(--muted);margin-top:8px}
.blog .section-title{padding-top:40px}
.post{position:absolute;top:130px;width:322px;height:408px;border:1px solid #e3e3e3;background:var(--white)}
.post .thumb{height:205px;background:linear-gradient(135deg,#e9eef2,#b9c4cc)}
.post .date{position:absolute;left:10px;top:180px;background:#d9381e;color:var(--white);font-size:11px;padding:5px 12px}
.post h3{font-size:19px;font-weight:700;color:var(--ink);line-height:24px;margin:20px 16px 10px}
.post p{font-size:11.5px;line-height:18px;color:var(--muted);margin:0 16px}
.post .btn{position:absolute;left:16px;bottom:30px;font-size:11px;padding:9px 16px}

/* team */
.team{top:2479px;height:446px;background:var(--orange)}
.lined-title{position:absolute;left:0;right:0;top:42px;display:flex;align-items:center;gap:24px;color:var(--white);font-size:23px;font-weight:700}
.lined-title::before,.lined-title::after{content:"";flex:1;height:1px;background:rgba(255,255,255,.8)}
.team .section-sub{position:absolute;left:0;right:0;top:86px;color:var(--white)}
.member{position:absolute;top:155px;width:188px;height:210px;background:var(--white);padding:8px}
.member .portrait{height:146px;background:linear-gradient(180deg,#cfd4d8,#9aa3aa)}
.member h4{text-align:center;font-size:13px;font-weight:700;color:var(--ink);margin-top:14px}
.member span{display:block;text-align:center;font-size:10.5px;color:var(--muted);margin-top:4px}

/* about */
.about{top:2925px;height:414px;background:var(--white)}
.about h2{position:absolute;left:0;top:85px;font-size:27px;font-weight:700;color:var(--ink)}
.about h2 span{color:var(--orange)}
.about p{position:absolute;left:0;width:500px;font-size:13px;line-height:23px;color:var(--muted)}
.about .p1{top:130px}
.about .p2{top:198px}
.about .btn{position:absolute;left:0;top:300px;font-size:11px;padding:8px 14px}
.about .group{position:absolute;left:531px;top:53px;width:499px;height:308px;border:4px solid #eee;background:linear-gradient(135deg,#e6e3df,#b8b0a6)}

/* testimonials */
.testimonials{top:3339px;height:475px;background:linear-gradient(180deg,#3a3a3a,#2c2c2c)}
.quote{position:absolute;top:123px;width:470px;height:162px;background:rgba(0,0,0,.45);padding:28px 30px 0 60px;color:#ddd;font-size:12px;line-height:22px}
.quote svg{position:absolute;left:24px;top:28px}
.quote::after{content:"";position:absolute;left:60px;bottom:-16px;border:16px solid transparent;border-top-color:rgba(0,0,0,.45);border-bottom:0}
.client{position:absolute;top:325px;display:flex;align-items:center;gap:18px;color:var(--white);font-size:12px}
.client .avatar{width:86px;height:86px;border-radius:50%;border:4px solid var(--orange);background:#d6d6d6}

/* partners */
.partners{top:3814px;height:264px;background:var(--white)}
.partners h2{position:absolute;left:0;right:0;top:46px;text-align:center;font-size:25px;font-weight:700;color:var(--ink)}
.partners h2 span{color:var(--green)}
.badge{position:absolute;top:128px;width:210px;height:84px;background:var(--badge);border-radius:4px}
.partner-arrow{position:absolute;top:154px;font-size:26px;color:#bbb}

/* footer */
.site-footer{top:4078px;height:279px;background:var(--footer);color:#bbb}
.col{position:absolute;top:36px;font-size:11px}
.col h4{display:flex;align-items:center;gap:10px;color:var(--white);font-size:12px;font-weight:700;margin-bottom:20px}
.col ul{list-style:none;line-height:25px}
.col input{display:block;width:210px;height:32px;border:0;margin-bottom:12px;padding:0 10px;font-size:11px;color:#999;background:var(--white)}
.col .btn{font-size:11px;padding:10px 14px}
.social{display:flex;gap:8px}
.social i{width:26px;height:26px;border-radius:50%;display:block;background:#555}
.contact li{display:flex;gap:10px;align-items:flex-start;line-height:25px}
.bottom-bar{top:4357px;height:44px;background:#151515;color:#999;font-size:11px;text-align:center;line-height:44px}
</style>
</head>
<body>

<header class="section site-header">
  <div class="wrap">
    <div class="logo"><i></i>corvahub</div>
    <nav class="nav">
      <span class="active">HOME</span><span>HOW IT WORKS</span><span>ABOUT US</span><span>OUR PARTNERS</span><span>FAQ</span><span>BLOG</span><span class="login">LOGIN</span>
    </nav>
  </div>
</header>

<section class="section hero">
  <div class="hero-photo" role="img" aria-label="Businessman's hands cupped around a network of people icons on a dark background"></div>
  <div class="wrap">
    <h1>THE FUTURE OF WORK IS HERE !</h1>
    <p>Available Quality talent on demand</p>
    <a class="btn btn-green" href="#">Get start now</a>
    <div class="hero-arrows">
      <svg width="20" height="20" viewBox="0 0 20 20"><path d="M13 4 7 10l6 6" stroke="#fff" stroke-width="2.5" fill="none"/></svg>
      <svg width="20" height="20" viewBox="0 0 20 20"><path d="M7 4l6 6-6 6" stroke="#fff" stroke-width="2.5" fill="none"/></svg>
    </div>
  </div>
</section>

<section class="section talent">
  <div class="wrap">
    <h2>AVAILABLE, QUALITY <span>TALENT ON DEMAND!</span></h2>
    <p>Corvahub helps professional contractors to maximise their earning potential whilst enabling organisations to connect &amp; directly hire on-demand talent in a much more efficient way than they do today.</p>
    <a class="btn btn-orange" href="#">JOIN NOW(it's free!)</a>
    <div class="feature" style="left:530px">
      <svg width="52" height="46" viewBox="0 0 52 46"><path d="M12 2h28l10 13-24 29L2 15z" fill="none" stroke="#3fa649" stroke-width="4"/><path d="M2 15h48M18 2l8 13 8-13M17 15l9 29 9-29" fill="none" stroke="#3fa649" stroke-width="3"/></svg>
      <h3>SKILLS MATCH</h3><a href="#">READ MORE ›</a>
    </div>
    <div class="feature" style="left:720px">
      <svg width="48" height="46" viewBox="0 0 48 46"><rect x="2" y="6" width="44" height="38" rx="3" fill="none" stroke="#3fa649" stroke-width="4"/><rect x="2" y="6" width="44" height="10" fill="#3fa649"/><path d="M13 1v10M35 1v10" stroke="#3fa649" stroke-width="4"/><g fill="#3fa649"><rect x="9" y="21" width="6" height="6"/><rect x="21" y="21" width="6" height="6"/><rect x="33" y="21" width="6" height="6"/><rect x="9" y="32" width="6" height="6"/><rect x="21" y="32" width="6" height="6"/><rect x="33" y="32" width="6" height="6"/></g></svg>
      <h3>CALENDAR</h3><a href="#">READ MORE ›</a>
    </div>
    <div class="feature" style="left:895px">
      <svg width="36" height="48" viewBox="0 0 36 48"><path d="M18 2C9 2 2 9 2 18c0 12 16 28 16 28s16-16 16-28C34 9 27 2 18 2z" fill="#3fa649"/><circle cx="18" cy="18" r="6" fill="#fff"/></svg>
      <h3>LOCATIONS</h3><a href="#">READ MORE ›</a>
    </div>
  </div>
</section>

<section class="section welcome">
  <div class="wrap">
    <div class="video" role="img" aria-label="Video still with a welcome banner reading 'To the future of contracting'">
      <svg class="play" width="48" height="34" viewBox="0 0 48 34"><rect width="48" height="34" rx="8" fill="#d9381e"/><path d="M19 10l12 7-12 7z" fill="#fff"/></svg>
    </div>
    <h2>WELCOME TO <span>CORVAHUB</span></h2>
    <p>Corvahub is a unique marketplace providing contractors and companies a platform to connect in real-time by exposing the "availability status". Through intuitive search Corvahub will instantly shortlist available contractors with matching skill criteria. This is an invaluable tool for companies finding the right people at the right time and at low cost!!</p>
    <a class="btn btn-green" href="#">GET STARTED NOW</a>
  </div>
</section>

<section class="section accounts">
  <div class="wrap">
    <div class="account account-contractor">
      <h2>I'M A CONTRACTOR</h2>
      <div class="sub">If you are looking for work</div>
      <div class="photo" role="img" aria-label="Business people shaking hands across a table"></div>
      <ul>
        <li><svg width="12" height="10" viewBox="0 0 12 10"><path d="M1 5l3.5 3.5L11 1" stroke="#fff" stroke-width="2" fill="none"/></svg>Increase utilisation by reducing idle time</li>
        <li><svg width="12" height="10" viewBox="0 0 12 10"><path d="M1 5l3.5 3.5L11 1" stroke="#fff" stroke-width="2" fill="none"/></svg>Choice of work based on offers received</li>
        <li><svg width="12" height="10" viewBox="0 0 12 10"><path d="M1 5l3.5 3.5L11 1" stroke="#fff" stroke-width="2" fill="none"/></svg>Increase earning potential by dealing direct with companies</li>
      </ul>
      <span class="btn-outline">JOIN FOR FREE ›</span>
    </div>
    <div class="account account-company">
      <h2>I'M A COMPANY</h2>
      <div class="sub">If you are looking for people</div>
      <div class="photo" role="img" aria-label="Team of colleagues in a bright office"></div>
      <ul>
        <li><svg width="12" height="10" viewBox="0 0 12 10"><path d="M1 5l3.5 3.5L11 1" stroke="#fff" stroke-width="2" fill="none"/></svg>Save time by reviewing qualified shortlist of skills &amp; availability</li>
        <li><svg width="12" height="10" viewBox="0 0 12 10"><path d="M1 5l3.5 3.5L11 1" stroke="#fff" stroke-width="2" fill="none"/></svg>Predictable market talent pools and access to active resources</li>
        <li><svg width="12" height="10" viewBox="0 0 12 10"><path d="M1 5l3.5 3.5L11 1" stroke="#fff" stroke-width="2" fill="none"/></svg>Negotiate rates directly with the contractor</li>
      </ul>
      <span class="btn-outline">JOIN FOR FREE ›</span>
    </div>
  </div>
</section>

<section class="section blog">
  <div class="wrap">
    <h2 class="section-title">OUR BLOG</h2>
    <p class="section-sub">Latest from blog</p>
    <article class="post" style="left:15px">
      <div class="thumb" role="img" aria-label="Office workers at a desk"></div>
      <span class="date">29 Mar 2015</span>
      <h3>The Best Tech Skills to List on Your Resume</h3>
      <p>Job hunting this year? Here are the tech skills hiring managers want.</p>
      <a class="btn btn-green" href="#">Read More ›</a>
    </article>
    <article class="post" style="left:367px">
      <div class="thumb" role="img" aria-label="Smiling professional in a suit"></div>
      <span class="date">07 Mar 2015</span>
      <h3>The top five in-demand cloud skills for 2016</h3>
      <p>There were an estimated 18 million cloud computing jobs globally.</p>
      <a class="btn btn-green" href="#">Read More ›</a>
    </article>
    <article class="post" style="left:719px">
      <div class="thumb" role="img" aria-label="Large group of business people"></div>
      <span class="date">04 Mar 2015</span>
      <h3>20 hot IT skills that will get you a raise</h3>
      <p>IT professionals are well-compensated, but 2016 looks set to bring even more.</p>
      <a class="btn btn-green" href="#">Read More ›</a>
    </article>
  </div>
</section>

<section class="section team">
  <div class="wrap">
    <h2 class="lined-title">THE CORVAHUB TEAM</h2>
    <p class="section-sub">Stay connected with us !</p>
    <div class="member" style="left:0"><div class="portrait" role="img" aria-label="Portrait of team member"></div><h4>MARISA DELVANE</h4><span>CEO &amp; Co-Founder</span></div>
    <div class="member" style="left:210px"><div class="portrait" role="img" aria-label="Portrait of team member"></div><h4>TOBIAS RENHART</h4><span>CTO &amp; Co-Founder</span></div>
    <div class="member" style="left:421px"><div class="portrait" role="img" aria-label="Portrait of team member"></div><h4>OWEN CASTRELL</h4><span>COO &amp; Advisory Board Member</span></div>
    <div class="member" style="left:632px"><div class="portrait" role="img" aria-label="Portrait of team member"></div><h4>IDRIS NORWELL</h4><span>Technical Expert</span></div>
    <div class="member" style="left:842px"><div class="portrait" role="img" aria-label="Portrait of team member"></div><h4>KIAN SOTELO</h4><span>Senior Developer</span></div>
  </div>
</section>

<section class="section about">
  <div class="wrap">
    <h2>ABOUT <span>US</span></h2>
    <p class="p1">Finally a platform where companies can connect directly with professional contractors. No agencies, no hidden fees, no fuss.</p>
    <p class="p2">Corvahub believes that contractors should be paid a fair market rate for their services and employers should be able to find contractors cheaper than they do today.</p>
    <a class="btn btn-orange" href="#">JOIN NOW(it's free!)</a>
    <div class="group" role="img" aria-label="Diverse group of smiling professionals"></div>
  </div>
</section>

<section class="section testimonials">
  <div class="wrap">
    <h2 class="lined-title">CLIENT TESTIMONIALS</h2>
    <div class="quote" style="left:30px">
      <svg width="20" height="16" viewBox="0 0 20 16"><path d="M0 16V9C0 4 3 1 8 0v3C5 4 4 6 4 8h4v8zM12 16V9c0-5 3-8 8-9v3c-3 1-4 3-4 5h4v8z" fill="#f7941d"/></svg>
      Laurel is a technologist and returned to the workforce after having kids; she was challenged for part-time work preferring a flexible schedule. Joining the recruitment industry it was thriving but she was consistently frustrated in trying to match available contractors.
    </div>
    <div class="quote" style="left:530px">
      <svg width="20" height="16" viewBox="0 0 20 16"><path d="M0 16V9C0 4 3 1 8 0v3C5 4 4 6 4 8h4v8zM12 16V9c0-5 3-8 8-9v3c-3 1-4 3-4 5h4v8z" fill="#3fa649"/></svg>
      Evan is a technologist and returned to the workforce after a long break; he was challenged for part-time work preferring a flexible schedule. Joining the recruitment industry it was thriving but he was consistently frustrated in trying to match available contractors.
    </div>
    <div class="client" style="left:50px"><div class="avatar" role="img" aria-label="Client portrait"></div>- Miss Laurel Finch</div>
    <div class="client" style="left:575px"><div class="avatar" role="img" aria-label="Client portrait" style="border-color:var(--green)"></div>- Evan Marlow</div>
  </div>
</section>

<section class="section partners">
  <div class="wrap">
    <h2>OUR STRATEGIC <span>PARTNERS</span></h2>
    <span class="partner-arrow" style="left:-10px">‹</span>
    <div class="badge" style="left:75px" role="img" aria-label="Partner badge"></div>
    <div class="badge" style="left:410px" role="img" aria-label="Partner badge"></div>
    <div class="badge" style="left:745px" role="img" aria-label="Partner badge"></div>
    <span class="partner-arrow" style="right:-10px">›</span>
  </div>
</section>

<footer class="section site-footer">
  <div class="wrap">
    <div class="col" style="left:0">
      <h4><svg width="14" height="14" viewBox="0 0 14 14"><path d="M1 3h12M1 7h12M1 11h12" stroke="#fff" stroke-width="2"/></svg>QUICK LINKS</h4>
      <ul><li>Home</li><li>How it works</li><li>About Us</li><li>Our Partners</li><li>FAQ</li><li>Blog</li></ul>
    </div>
    <div class="col" style="left:200px">
      <h4><svg width="14" height="12" viewBox="0 0 14 12"><rect x="1" y="1" width="12" height="10" fill="none" stroke="#fff" stroke-width="1.6"/><path d="M1 1l6 5 6-5" stroke="#fff" stroke-width="1.6" fill="none"/></svg>NEWSLETTER SIGN UP</h4>
      <input type="text" value="Your Name" readonly>
      <input type="text" value="Your Email" readonly>
      <a class="btn btn-orange" href="#">SUBSCRIBE NOW</a>
    </div>
    <div class="col" style="left:500px">
      <h4><svg width="14" height="14" viewBox="0 0 14 14"><path d="M2 12L12 2M5 2h7v7" stroke="#fff" stroke-width="2" fill="none"/></svg>FOLLOW US</h4>
      <div class="social"><i></i><i></i><i></i><i></i><i></i><i></i></div>
    </div>
    <div class="col contact" style="left:770px">
      <h4><svg width="14" height="14" viewBox="0 0 14 14"><circle cx="7" cy="7" r="6" fill="none" stroke="#fff" stroke-width="1.6"/><circle cx="7" cy="7" r="2" fill="#fff"/></svg>CONTACT US</h4>
      <ul>
        <li><svg width="10" height="14" viewBox="0 0 10 14" style="margin-top:6px"><path d="M5 0C2 0 0 2 0 5c0 4 5 9 5 9s5-5 5-9c0-3-2-5-5-5z" fill="#bbb"/></svg>Office: Office Address, City Address,<br>State, Country Code</li>
        <li><svg width="10" height="14" viewBox="0 0 10 14" style="margin-top:6px"><rect x="1" y="0" width="8" height="14" rx="1.5" fill="#bbb"/></svg>Mobile: 555-0142-880</li>
        <li><svg width="10" height="14" viewBox="0 0 10 14" style="margin-top:6px"><rect x="0" y="3" width="10" height="8" fill="#bbb"/></svg>Fax: 555-0142-881</li>
        <li><svg width="10" height="14" viewBox="0 0 10 14" style="margin-top:6px"><rect x="0" y="3" width="10" height="8" fill="none" stroke="#bbb" stroke-width="1.4"/></svg>Mail: hello@corvahub-mail.com</li>
      </ul>
    </div>
  </div>
</footer>
<div class="section bottom-bar">CORVAHUB © 2016 | Privacy Policy</div>

</body>
</html>
```